Christmas Candle Label

We require a Christmas candle label that fits with our current brand (see larkfieldcandleworks.com.au, and also example attached). On the attached we would like the word 'Marlowe - Pendleby' replaced with 'Merry Christmas' (or something creative that you can come up with) and the writing on the left hand side 'lose yourself in the subtle.........' replaced with 'its beginning to smell a lot like Christmas' (or something creative that you can come up with). We would like the flora image in the background replaced with a line drawing of a Christmas tree or holy or anything else that is appropriate. Finally we are not sure if a different colour label i.e. red, maroon or green (with lots of black, silver or gold writing) instead of black would be best for this label. It may be best to see a comparison of our original black label with black, silver or gold writing, and the other colours.

```html
<!DOCTYPE html>
<html lang="en">
<head>
<meta charset="UTF-8">
<title>Christmas Candle Label</title>
<link rel="stylesheet" href="https://fonts.googleapis.com/css2?family=Mali:wght@300&family=Poppins:wght@300&display=swap">
<style>
  :root {
    --backdrop: #d9dbd2;
    --label-maroon: #431019;
    --label-maroon-deep: #3a0d15;
    --gold-light: #e3b469;
    --gold: #c9954a;
    --gold-dark: #9c6c2c;
    --text-white: #f5efe9;
    --floral-tone: #5b2530;
    --tree-tone: #6e3c42;
  }
  * { margin: 0; padding: 0; box-sizing: border-box; }
  html, body {
    width: 1200px;
    height: 1200px;
    overflow: hidden;
  }
  body {
    background: var(--backdrop);
    position: relative;
  }
  .candle-label {
    position: absolute;
    left: 50px;
    top: 380px;
    width: 1100px;
    height: 440px;
    background: linear-gradient(90deg, var(--label-maroon) 0%, var(--label-maroon-deep) 100%);
    overflow: hidden;
  }
  .floral-artwork {
    position: absolute;
    left: 124px;
    top: 47px;
    width: 310px;
    height: 393px;
    background: linear-gradient(180deg, rgba(91, 37, 48, 0.55) 0%, var(--floral-tone) 50%, rgba(91, 37, 48, 0.55) 100%);
    border-radius: 6px;
  }
  .tree-artwork {
    position: absolute;
    left: 858px;
    top: 34px;
    width: 242px;
    height: 406px;
    background: linear-gradient(180deg, rgba(110, 60, 66, 0.6) 0%, var(--tree-tone) 55%, rgba(110, 60, 66, 0.6) 100%);
    border-radius: 6px;
  }
  .tagline {
    position: absolute;
    left: 65px;
    top: 150px;
    font-family: 'Poppins', sans-serif;
    font-weight: 300;
    font-size: 23px;
    line-height: 29px;
    letter-spacing: 0.14em;
    color: var(--text-white);
  }
  .greeting {
    font-family: 'Mali', cursive;
    font-weight: 300;
    font-size: 86px;
    line-height: 86px;
  }
  .greeting-line {
    position: absolute;
    white-space: nowrap;
    transform: translateX(-50%);
    background: linear-gradient(100deg, var(--gold-dark) 0%, var(--gold-light) 45%, var(--gold) 70%, var(--gold-dark) 100%);
    -webkit-background-clip: text;
    background-clip: text;
    color: transparent;
  }
  .greeting-line--first {
    left: 628px;
    top: 74px;
  }
  .greeting-line--second {
    left: 599px;
    top: 186px;
  }
  .gold-rule {
    position: absolute;
    left: 586px;
    top: 319px;
    width: 204px;
    height: 2px;
    background: linear-gradient(90deg, var(--gold-dark), var(--gold-light), var(--gold));
  }
  .product-name {
    position: absolute;
    left: 480px;
    top: 354px;
    font-family: 'Poppins', sans-serif;
    font-weight: 300;
    font-size: 20px;
    letter-spacing: 0.14em;
    color: var(--text-white);
  }
</style>
</head>
<body>
  <section class="candle-label">
    <div class="floral-artwork" role="img" aria-label="Fine line drawing of lilies and stems"></div>
    <div class="tree-artwork" role="img" aria-label="Swirling ribbon line drawing of a Christmas tree with white stars and sparkles"></div>
    <p class="tagline">its beginning<br>to smell a<br>lot like<br>Christmas</p>
    <h1 class="greeting">
      <span class="greeting-line greeting-line--first">Merry</span>
      <span class="greeting-line greeting-line--second">Christmas</span>
    </h1>
    <div class="gold-rule"></div>
    <p class="product-name">Handmade Candle</p>
  </section>
</body>
</html>
```